Redesign Craft Brewing Recipe Website

Originally built with Bootstrap just to get the site going, I am seeking a complete redesign of the sites home page and recipe page. I am an experienced web developer with no graphic background, initially just looking for psd mocks.

I prefer styles that are clean and modern, and would prefer anything that is fun, engaging, and has an organic feel to it. I currently have a cartoon rabbit as a logo, but it needs some modification/tweaking, so any help in that area would be great as well.

Current site:
http://kettlewren.plumhostsite.net/

Current launch page/logo:
http://www.kettlewren.com/

I like the overall layout of the elements currently, but the design sucks.

The launch page is at the following URL

Reason: Still looking for a more modern design. Designs received so far are too similar to the original.

My site is content based and does not contain images or products. Your design should not consist of large images.

Reason: The website has very little images, so the designs need to be more text and content based. The header needs to be very small and should not contain an ad rotater.

Target Market(s)

Home brewers, Craft brewers, Microbreweries, Brewpubs

Requirements
Must have
• Web 2.0 Look and Feel, Fun, Hip, Focus on content
Should not have
• A large photo as a header

```html
<!DOCTYPE html>
<html lang="en">
<head>
<meta charset="utf-8">
<title>Kettlewren – Home</title>
<link rel="stylesheet" href="https://fonts.googleapis.com/css2?family=Dosis:wght@400;500;600;700&display=swap">
<style>
  :root {
    --backdrop: #f1f3f4;
    --navy: #02587a;
    --panel: #045a7a;
    --sky-top: #00b9f2;
    --sky-bottom: #0078a6;
    --orange: #ff5a1f;
    --white: #ffffff;
    --ink: #0a5f86;
  }
  * { box-sizing: border-box; margin: 0; padding: 0; }
  html, body { width: 1200px; height: 1200px; overflow: hidden; }
  body {
    position: relative;
    font-family: "Dosis", sans-serif;
    background: var(--backdrop);
    color: var(--white);
  }

  /* Page frame */
  .page {
    position: absolute; left: 0; top: 323px; width: 1200px; height: 554px;
    overflow: hidden;
    background: linear-gradient(to bottom, var(--sky-top) 0%, #0096cc 45%, var(--sky-bottom) 100%);
  }

  /* Top navigation */
  .site-nav {
    position: absolute; left: 0; top: 0; width: 1200px; height: 44px;
    background: var(--navy);
  }
  .site-nav .brand {
    position: absolute; left: 275px; top: 8px;
    font-size: 26px; font-weight: 500; letter-spacing: 0.4px; line-height: 28px;
    color: var(--white);
  }
  .site-nav .menu { position: absolute; left: 449px; top: 14px; display: flex; gap: 24px; list-style: none; }
  .site-nav .menu a { font-size: 12px; font-weight: 500; line-height: 16px; color: var(--white); text-decoration: none; text-transform: uppercase; }
  .site-nav .menu a.is-active { color: var(--orange); }
  .site-nav .login {
    position: absolute; right: 273px; top: 12px;
    font-size: 16px; font-weight: 700; line-height: 20px; color: var(--white); text-decoration: none;
  }

  /* Hero */
  .hero {
    position: absolute; left: 274px; top: 64px; width: 653px; height: 127px;
    background: var(--panel); padding: 22px 25px;
  }
  .hero .title { font-size: 44px; font-weight: 500; line-height: 42px; letter-spacing: 0.5px; }
  .hero .tagline { font-size: 14px; font-weight: 500; line-height: 16px; margin-top: 2px; }
  .hero .like { display: flex; align-items: center; gap: 4px; margin-top: 9px; font-size: 9px; line-height: 11px; }
  .hero .like .dot { width: 11px; height: 11px; background: var(--white); border-radius: 2px; }

  /* Sidebar */
  .sidebar {
    position: absolute; left: 274px; top: 215px; width: 162px; height: 339px;
    background: var(--panel);
  }
  .sidebar .search-field {
    position: absolute; left: 12px; top: 13px; width: 138px; height: 21px;
    background: var(--white); border: none;
  }
  .sidebar .search-go {
    position: absolute; left: 124px; top: 40px; width: 26px; height: 27px;
    background: var(--orange); color: var(--white); border: none;
    font-family: "Dosis", sans-serif; font-size: 16px; font-weight: 700; line-height: 27px;
  }
  .sidebar .filters { position: absolute; left: 12px; top: 80px; list-style: none; }
  .sidebar .filters li { display: flex; align-items: center; gap: 5px; height: 29.5px; font-size: 12px; font-weight: 500; }
  .sidebar .filters .box { width: 9px; height: 9px; background: var(--white); }

  /* Tabs */
  .tabs { position: absolute; left: 450px; top: 216px; display: flex; gap: 9px; }
  .tabs .tab {
    width: 83px; height: 31px; display: flex; align-items: center; justify-content: center;
    font-size: 12px; font-weight: 500; text-transform: uppercase; background: var(--panel);
  }
  .tabs .tab.is-active { background: var(--orange); }

  /* Recipe cards */
  .recipe-card {
    position: absolute; left: 450px; width: 477px; height: 78px;
    background: var(--white); color: var(--ink); padding: 16px 9px;
  }
  .recipe-card .name { font-size: 15px; font-weight: 500; text-transform: uppercase; line-height: 19px; }
  .recipe-card .summary { font-size: 14px; font-weight: 500; line-height: 19px; }
  .card-1 { top: 258px; }
  .card-2 { top: 357px; }
  .card-3 { top: 457px; }
</style>
</head>
<body>
  <main class="page">
    <header class="site-nav">
      <div class="brand">KETTLEWREN</div>
      <ul class="menu">
        <li><a class="is-active" href="#">Home</a></li>
        <li><a href="#">Recipies</a></li>
      </ul>
      <a class="login" href="#">LOGIN</a>
    </header>

    <section class="hero">
      <h1 class="title">KETTLEWREN</h1>
      <p class="tagline">Kettlewren is the easiest way to create and share craft beer recipies</p>
      <div class="like"><span class="dot"></span>like</div>
    </section>

    <aside class="sidebar">
      <input class="search-field" type="text" aria-label="Search">
      <button class="search-go">Go</button>
      <ul class="filters">
        <li>Brewing <span class="box"></span></li>
        <li>Styles <span class="box"></span></li>
        <li>Match Maker <span class="box"></span></li>
      </ul>
    </aside>

    <nav class="tabs">
      <div class="tab is-active">Recent</div>
      <div class="tab">Popular</div>
    </nav>

    <article class="recipe-card card-1">
      <h2 class="name">Recipie 1</h2>
      <p class="summary">Recipie Description etc.</p>
    </article>
    <article class="recipe-card card-2">
      <h2 class="name">Recipie 2</h2>
      <p class="summary">Recipie Description etc.</p>
    </article>
    <article class="recipe-card card-3">
      <h2 class="name">Recipie 3</h2>
      <p class="summary">Recipie Description etc.</p>
    </article>
  </main>
</body>
</html>
```